Business card required for IT Consultancy Business - Tealbrook Consulting.
Company provides the whole nine yards of services across IT Architecture, design and execution.
Basically we provide consulting services to help businesses make sure their technology is enabling their business strategy.
Design for front and back required.
We would like the front of the card to inlcude:
Name
Title
Mobile number
email address
www.tbkc.com.au
Company logos attached.
Thank you
Industry/Entity Type
Business
Contact Information for Business Card
Name
Title
Mobile number
email address
www.tbkc.com.au
Look and feel
Each slider illustrates characteristics of the customer's brand and the style your logo design should communicate.

```html
<!DOCTYPE html>
<html lang="en">
<head>
<meta charset="utf-8">
<title>Tealbrook Consulting – Business Card</title>
<link rel="stylesheet" href="https://fonts.googleapis.com/css2?family=Roboto:wght@400;500;700&family=Montserrat:wght@600&display=swap">
<style>
  :root {
    --backdrop: #2b2b2b;
    --brand-blue: #116fb6;
    --brand-orange: #e8572a;
    --paper: #f3f3f3;
    --white: #ffffff;
  }
  * { margin: 0; padding: 0; box-sizing: border-box; }
  html, body { width: 1200px; height: 960px; overflow: hidden; }
  body { background: var(--backdrop); position: relative; font-family: "Roboto", Arial, sans-serif; }

  .card {
    position: absolute;
    width: 600px;
    height: 342px;
    overflow: hidden;
    box-shadow: 0 3px 8px rgba(0,0,0,0.5);
  }
  .card--front { left: 314px; top: 113px; background: var(--paper); }
  .card--back  { left: 311px; top: 472px; background: var(--brand-orange); }

  .front-shapes { position: absolute; inset: 0; }

  .contact-block {
    position: absolute;
    left: 48px;
    top: 44px;
    color: var(--white);
  }
  .contact-name { font-size: 20px; font-weight: 500; letter-spacing: 0.2px; line-height: 24px; }
  .contact-title { font-size: 15px; font-weight: 400; line-height: 20px; margin-bottom: 12px; }
  .contact-list { list-style: none; font-size: 14px; line-height: 19px; }
  .contact-list li { display: flex; align-items: center; gap: 6px; }
  .contact-list svg { width: 13px; height: 13px; flex: none; }

  .brand-name {
    position: absolute;
    font-family: "Montserrat", Arial, sans-serif;
    font-weight: 600;
    text-align: right;
    line-height: 1.05;
  }
  .card--front .brand-name {
    right: 56px;
    top: 216px;
    font-size: 28px;
    color: var(--brand-blue);
  }
  .card--back .brand-name {
    right: 42px;
    top: 212px;
    font-size: 36px;
    color: var(--white);
  }
  .back-url {
    position: absolute;
    right: 44px;
    top: 298px;
    font-size: 14px;
    letter-spacing: 4.5px;
    color: var(--white);
  }
</style>
</head>
<body>

  <section class="card card--front" aria-label="Card front">
    <svg class="front-shapes" viewBox="0 0 600 342" aria-hidden="true">
      <polygon points="0,0 404,0 154,342 0,342" fill="var(--brand-blue)"/>
      <polygon points="411,0 423,0 173,342 161,342" fill="var(--brand-orange)"/>
    </svg>

    <div class="contact-block">
      <p class="contact-name">DANIEL HARTLEY</p>
      <p class="contact-title">CEO/FOUNDER</p>
      <ul class="contact-list">
        <li>
          <svg viewBox="0 0 13 13"><rect x="3" y="0.5" width="7" height="12" rx="1.2" fill="none" stroke="#fff" stroke-width="1.3"/><circle cx="6.5" cy="10.3" r="0.8" fill="#fff"/></svg>
          836 555 0142
        </li>
        <li>
          <svg viewBox="0 0 13 13"><rect x="0.5" y="3" width="12" height="8" fill="#fff"/><polyline points="0.5,3 6.5,7.5 12.5,3" fill="none" stroke="var(--brand-blue)" stroke-width="1"/></svg>
          hello@tbkc.com.au
        </li>
        <li>
          <svg viewBox="0 0 13 13"><circle cx="6.5" cy="6.5" r="6" fill="#fff"/><path d="M3 4.5c1.5 0 2 1 1.5 2s1 2 1 3.5M8 2c0 1.5 1.5 2 2.5 2.5M9 8c1 0 1.5 1 1 2" fill="none" stroke="var(--brand-blue)" stroke-width="1.2"/></svg>
          www.tbkc.com.au
        </li>
      </ul>
    </div>

    <p class="brand-name">Tealbrook<br>Consulting</p>
  </section>

  <section class="card card--back" aria-label="Card back">
    <p class="brand-name">Tealbrook<br>Consulting</p>
    <p class="back-url">www.tbkc.com.au</p>
  </section>

</body>
</html>
```